Re-design of website: www.veltramedia.ca/en/

Veltrameda B is a promotional agency specializing in on-site marketing. We are re-designing their website.

We have already produced a prototype:
http://norvapixel.com/veltramedia_siteweb/

The architecture in the prototype must be respected. Please dress up the design with green, grey and black circles and other textures found on their current website www.veltramedia.ca

Inspiration for design that we like, clean, flat design:

- http://www.brimfoxlab.co/
- http://quellarworks.com/#!/process
- http://wearetolvane.com/

Delivrables: PSD files of each page of the prototype

Here are the images of their print portfolio: http://ftp.veltramedia.ca/clients/VLM/VELTRAMEDIA-PORTFOLIO-2012_EN.zip

Industry/Entity Type

Architecture

Requirements
Must have
• Responsive Design

```html
<!DOCTYPE html>
<html lang="fr">
<head>
<meta charset="utf-8">
<title>Veltrameda B</title>
<link rel="stylesheet" href="https://fonts.googleapis.com/css2?family=Bebas+Neue&family=Oswald:wght@400;500&family=Open+Sans:wght@400&display=swap">
<style>
:root{
  --green:#9ccd63;
  --green-deep:#8cc153;
  --green-light:#b6dd86;
  --white:#ffffff;
  --ink:#4f4f4f;
  --grey:#6b6b6b;
  --rule:#d6d6d6;
  --photo-a:#8a7a6e;
  --photo-b:#5f5a58;
}
*{margin:0;padding:0;box-sizing:border-box}
html,body{width:1200px;height:2299px;overflow:hidden;background:var(--white)}
body{position:relative;font-family:"Open Sans",Arial,sans-serif;color:var(--ink)}
.site-header{position:absolute;top:0;left:0;width:1200px;height:154px;background:var(--white)}
.brand{position:absolute;top:26px;left:0;width:1200px;text-align:center}
.brand-name{font-family:"Oswald",Arial,sans-serif;font-weight:500;font-size:36px;letter-spacing:3px;color:var(--ink);line-height:48px}
.main-nav{position:absolute;top:106px;left:0;width:1200px;display:flex;justify-content:center;gap:19px}
.main-nav a{font-family:"Oswald",Arial,sans-serif;font-size:21px;color:var(--ink);text-decoration:none;letter-spacing:.3px}
.hero{position:absolute;top:154px;left:0;width:1200px;height:492px;
  background:
    radial-gradient(ellipse 380px 200px at 600px 0,rgba(255,255,255,.28),transparent 80%),
    radial-gradient(ellipse 700px 380px at 600px 250px,transparent 55%,rgba(90,140,40,.18)),
    linear-gradient(180deg,var(--green) 0%,var(--green-deep) 100%)}
.hero-title{position:absolute;top:112px;left:0;width:1200px;text-align:center;font-family:"Bebas Neue",Impact,sans-serif;font-weight:400;font-size:76px;line-height:86px;color:var(--white);letter-spacing:1px}
.section-title{position:absolute;top:676px;left:0;width:1200px;text-align:center;font-family:"Oswald",Arial,sans-serif;font-weight:500;font-size:40px;color:var(--grey)}
.section-rule{position:absolute;top:750px;left:129px;width:940px;height:3px;background:var(--rule)}
.gallery{position:absolute;top:779px;left:129px;display:grid;grid-template-columns:repeat(3,302px);column-gap:18px;row-gap:30px}
.gallery-item{width:302px;height:250px;border-top:8px solid var(--green);background:linear-gradient(160deg,var(--photo-a),var(--photo-b))}
.team-bands{position:absolute;top:1411px;left:0}
.card-title{position:absolute;width:302px;height:70px;font-family:"Bebas Neue",Impact,sans-serif;font-weight:400;font-size:44px;line-height:72px;text-align:center}
.card-title.on-green{background:var(--white);color:var(--green)}
.card-title.on-white{background:var(--green);color:var(--white)}
.card-text{position:absolute;width:302px;font-family:Arial,Helvetica,sans-serif;font-size:12.5px;line-height:17px;letter-spacing:-.1px}
.card-text.on-green{color:var(--white)}
.card-text.on-white{color:var(--grey)}
.member{position:absolute;width:136px;text-align:center;font-family:"Oswald",Arial,sans-serif;line-height:1.3}
.member-name{font-size:13px;font-weight:500}
.member-role{font-size:9.5px}
.member.dark{color:var(--ink)}
.member.light{color:var(--white)}
.site-footer{position:absolute;top:2198px;left:0;width:1200px;display:flex;justify-content:center;gap:30px;font-size:14px;color:var(--white)}
</style>
</head>
<body>
<header class="site-header">
  <div class="brand"><span class="brand-name">VELTRAMEDA B</span></div>
  <nav class="main-nav">
    <a href="#">AGENCE</a><a href="#">SERVICES</a><a href="#">REALISATIONS</a><a href="#">EVENEMENTS</a><a href="#">RECRUTMENTS</a><a href="#">CONTACT</a>
  </nav>
</header>

<section class="hero">
  <h1 class="hero-title">Lorem ipsum dolor sitamet,<br>consectetur adip sicing elit,<br>sed do eiusmod tempor incid</h1>
</section>

<h2 class="section-title">NOS RÉALISATIONS 360</h2>
<div class="section-rule"></div>
<div class="gallery">
  <div class="gallery-item" role="img" aria-label="Photo d'événement promotionnel en extérieur"></div>
  <div class="gallery-item" role="img" aria-label="Photo de dégustation sur un stationnement"></div>
  <div class="gallery-item" role="img" aria-label="Photo d'animatrices en tuque"></div>
  <div class="gallery-item" role="img" aria-label="Photo d'hôtesses en uniforme"></div>
  <div class="gallery-item" role="img" aria-label="Photo de participants à une soirée"></div>
  <div class="gallery-item" role="img" aria-label="Photo d'animation en épicerie"></div>
</div>

<svg class="team-bands" width="1200" height="888" viewBox="0 1411 1200 888" aria-hidden="true">
  <rect x="0" y="1411" width="1200" height="287" fill="var(--green)"/>
  <rect x="0" y="2078" width="1200" height="221" fill="var(--green)"/>
  <g fill="var(--green)">
    <circle cx="280" cy="1641" r="127"/><circle cx="600" cy="1641" r="127"/><circle cx="920" cy="1641" r="127"/>
  </g>
  <g fill="var(--white)">
    <circle cx="280" cy="1651" r="68"/><circle cx="600" cy="1651" r="68"/><circle cx="920" cy="1651" r="68"/>
    <circle cx="280" cy="2010" r="127"/><circle cx="600" cy="2010" r="127"/><circle cx="920" cy="2010" r="127"/>
  </g>
  <g fill="var(--green)">
    <circle cx="280" cy="2020" r="68"/><circle cx="600" cy="2020" r="68"/><circle cx="920" cy="2020" r="68"/>
  </g>
</svg>

<div class="card-title on-green" style="top:1440px;left:129px">CONTACT</div>
<div class="card-title on-green" style="top:1440px;left:449px">RECRUTMENT</div>
<div class="card-title on-green" style="top:1440px;left:769px">SUIVEZ-NOUS</div>
<p class="card-text on-green" style="top:1526px;left:129px">Lorem ipsum dolor sit amet, consectetur adipisicing elit, sed do eiusmod tempor incididunt ut labore.</p>
<p class="card-text on-green" style="top:1526px;left:449px">Lorem ipsum dolor sit amet, consectetur adipisicing elit, sed do eiusmod tempor incididunt ut labore.</p>
<p class="card-text on-green" style="top:1526px;left:769px">Lorem ipsum dolor sit amet, consectetur adipisicing elit, sed do eiusmod tempor incididunt ut labore.</p>
<div class="member dark" style="top:1635px;left:212px"><div class="member-name">ÉTIENNE MOREL</div><div class="member-role">PRÉSIDENT</div></div>
<div class="member dark" style="top:1635px;left:532px"><div class="member-name">LINA DUFORT</div><div class="member-role">VICE-PRÉSIDENTE</div></div>
<div class="member dark" style="top:1635px;left:852px"><div class="member-name">CLAIRE DUBREUIL</div><div class="member-role">CHEF DE PROJETS MARKETING</div></div>

<div class="card-title on-white" style="top:1810px;left:129px">RECRUTMENT</div>
<div class="card-title on-white" style="top:1810px;left:449px">SUIVEZ-NOUS</div>
<div class="card-title on-white" style="top:1810px;left:769px">CONTACT</div>
<p class="card-text on-white" style="top:1896px;left:129px">Lorem ipsum dolor sit amet, consectetur adipisicing elit, sed do eiusmod tempor incididunt ut labore.</p>
<p class="card-text on-white" style="top:1896px;left:449px">Lorem ipsum dolor sit amet, consectetur adipisicing elit, sed do eiusmod tempor incididunt ut labore.</p>
<p class="card-text on-white" style="top:1896px;left:769px">Lorem ipsum dolor sit amet, consectetur adipisicing elit, sed do eiusmod tempor incididunt ut labore.</p>
<div class="member light" style="top:2004px;left:212px"><div class="member-name">NOÉMIE TARDIF</div><div class="member-role">COORDINATRICE MARKETING</div></div>
<div class="member light" style="top:2004px;left:532px"><div class="member-name">NOÉMIE TARDIF</div><div class="member-role">COORDINATRICE MARKETING</div></div>
<div class="member light" style="top:2004px;left:852px"><div class="member-name">NOÉMIE TARDIF</div><div class="member-role">COORDINATRICE MARKETING</div></div>

<footer class="site-footer"><span>@Copyright</span><span>All rights reserved</span></footer>
</body>
</html>
```